Hypnotherapy- past life regression-life between lives therapist needs a website

I need a website that is enticing and spiritual in its feeling. It needs to have a lot of beautiful nature pictures included. The theme is "Quiet Harbor Path- what might you find....Lessons Solutions Answers"
Because all of us have the answers to living our best life, they are in our subconcious. But not everyone is capable of accessing them. Hypnosis accesses the subconcious and helps to create new neural pathways in the brain which can create new behaviors and responses to situations.
Hypnosis can help with anxiety, pain relief, weight loss, smoking/vaping cessation, self confidence......anything about yourself that you want to change.
Exploration of past lives and life between lives can reveal things related to ones current life. For example, perhaps your fear of deep water is a result of drowning in a past life. Once this has been discovered, it can lead to changes in ones current life.
Almost any personal behavior one wants to change, can be helped through hypnotherapy.
I need a page for testimonials, a place for scheduling (I will have a link to my scheduling app) some information about hypnotherapy.
I am uploading my logo files. My business card will be using the black and gold style, but my website does not have to reflect that. It can be based on the caramel and deep green like full color logo. Earthy, calm colors.
I also like the mock up of my logo on the beach and there was one on a starry night sky that I also liked.
Target Market(s)
men and women ages 25-50
Industry/Entity Type
natural health and wellness, spirituality
Number of Pages Required
4 page
Requirements
Must have
- a page for testimonials, perhaps with a beautiful nature picture with each one, I will have approximately 6. A link to schedule a complimentary intro session, preferably on the first page
Should not have
- no swinging watches or other sterotyped hypnosis symbols

```html
<!DOCTYPE html>
<html lang="en">
<head>
<meta charset="utf-8">
<title>Quiet Harbor Path — Hypnotherapy</title>
<link href="https://fonts.googleapis.com/css2?family=Libre+Baskerville:wght@400;700&family=Cormorant+Garamond:wght@500&family=Poppins:wght@300;400;500;600&family=Parisienne&display=swap" rel="stylesheet">
<style>
:root{
  --orange:#e5872a;
  --ink:#262421;
  --muted:#4d4a45;
  --cream:#f3f2ec;
  --mist:#f7f7f5;
  --footer:#1d1b16;
  --white:#ffffff;
}
*{box-sizing:border-box;margin:0;padding:0}
html,body{width:1200px;height:3710px;overflow:hidden}
body{position:relative;background:var(--white);font-family:'Poppins',sans-serif;color:var(--ink)}
.abs{position:absolute}
.serif-head{font-family:'Libre Baskerville',serif;font-weight:700;color:var(--ink);letter-spacing:.5px}
.btn{position:absolute;display:flex;align-items:center;justify-content:center;background:var(--orange);color:var(--white);font-size:13px;font-weight:600;text-transform:uppercase;letter-spacing:.3px;text-decoration:none}

/* hero */
.hero{left:0;top:0;width:1200px;height:660px;background:linear-gradient(180deg,#5d7a86 0%,#7f98a0 25%,#8ea7ac 42%,#4e6b73 60%,#6b8489 78%,#9aa9a8 100%)}
.hero::after{content:"";position:absolute;inset:0;background:linear-gradient(90deg,rgba(80,60,30,.45),rgba(0,0,0,0) 30%,rgba(0,0,0,0) 70%,rgba(170,110,40,.45))}
.brand{left:112px;top:44px;display:flex;align-items:center;gap:10px;color:var(--white);font-family:'Libre Baskerville',serif;font-weight:700;font-size:17px;z-index:2;width:180px;line-height:1.2}
.brand-dot{width:14px;height:14px;border-radius:50%;background:var(--white);flex:none}
.nav{left:545px;top:36px;display:flex;gap:0;z-index:2}
.nav a{color:var(--white);font-size:14px;text-decoration:none;padding:0 9.5px}
.nav a.active{font-weight:600}
.book{left:946px;top:27px;width:143px;height:41px;z-index:2}
.hero-title{left:0;width:1200px;top:395px;text-align:center;color:var(--white);font-family:'Cormorant Garamond',serif;font-weight:500;font-size:48px;letter-spacing:1px;z-index:2}
.hero-sub{left:0;width:1200px;top:455px;text-align:center;color:var(--white);font-size:23px;font-weight:300;z-index:2}
.chev{left:590px;top:533px;z-index:2}

/* about */
.about-bg{left:0;top:560px;z-index:1}
.about-head{left:114px;top:676px;font-size:39px;z-index:2}
.about-text{left:395px;top:676px;width:700px;font-size:15px;line-height:28.5px;color:var(--muted);z-index:2}
.about-photo{left:245px;top:799px;width:708px;height:382px;background:linear-gradient(180deg,#8a8f52 0%,#4d5a33 35%,#2a3320 70%,#1c2215 100%);box-shadow:0 6px 16px rgba(0,0,0,.25);z-index:2}
.prints{left:960px;top:795px;width:240px;height:260px;background:radial-gradient(ellipse at 60% 50%,rgba(170,170,165,.28),rgba(170,170,165,0) 70%);z-index:2}

/* hypnotherapy */
.hyp-head{left:112px;top:1295px;font-size:39px}
.hyp-script{left:112px;top:1362px;width:560px;font-family:'Parisienne',cursive;font-size:32px;line-height:41px;color:var(--ink)}
.hyp-text{left:112px;top:1462px;width:545px;font-size:15px;line-height:28.5px;color:var(--muted)}
.hyp-btn{left:112px;top:1660px;width:143px;height:42px}
.hyp-back{left:726px;top:1293px;width:311px;height:447px;background:#fdf7f2}
.hyp-photo{left:778px;top:1243px;width:309px;height:446px;background:linear-gradient(160deg,#e6d8cc 0%,#d8b7a0 45%,#d58b5a 75%,#e0a06a 100%)}

/* heal */
.heal{left:0;top:1810px;width:1200px;height:559px;background:var(--mist)}
.heal-head{left:0;width:1200px;top:1875px;text-align:center;font-size:39px}
.cond{position:absolute;width:212px;text-align:center;font-size:20px;line-height:30px;font-weight:400;color:var(--ink)}
.cond svg{display:block;margin:0 auto 10px}
.heal-btn{left:528px;top:2274px;width:143px;height:42px}

/* testimonials */
.say-head{left:0;width:1200px;top:2446px;text-align:center;font-size:39px}
.card{position:absolute;top:2552px;width:468px;height:272px;background:var(--white);border:1px solid #d9d9d9;border-radius:12px;overflow:hidden}
.card.focus{border:none;box-shadow:0 8px 26px rgba(0,0,0,.12)}
.avatar{position:absolute;left:22px;top:28px;width:101px;height:101px;border-radius:50%;background:linear-gradient(180deg,#9eb2b8,#6a6a58)}
.qmark{position:absolute;left:28px;top:150px;width:80px;height:56px;background:linear-gradient(90deg,rgba(229,135,42,.18),rgba(229,135,42,.28));border-radius:6px}
.c-name{position:absolute;left:148px;top:36px;font-size:19px;font-weight:500}
.stars{position:absolute;left:148px;top:70px;display:flex;gap:2px}
.c-text{position:absolute;left:149px;top:98px;width:300px;font-size:15.5px;line-height:30px;color:var(--muted)}
.c-text b{color:var(--orange);font-weight:600}
.corner{position:absolute;right:0;bottom:0;width:20px;height:20px;background:#f3c59a;border-top-left-radius:10px}
.card:not(.focus) .corner{background:#dcdcdc}
.arrows{left:535px;top:2868px;z-index:2}

/* quote */
.quote-photo{left:0;top:2858px;width:1200px;height:590px;background:linear-gradient(180deg,#ffffff 0%,#c9d2d6 12%,#8aa0ad 28%,#6f7f7e 45%,#8e7658 62%,#5a4a33 80%,#2c2418 100%)}
.quote-head{left:108px;top:3058px;color:var(--white);font-size:39px;z-index:2}
.field{position:absolute;left:112px;width:350px;background:var(--white);font-size:13px;color:#666;padding:12px 24px;z-index:2}
.quote-btn{left:111px;top:3339px;width:143px;height:41px;z-index:2}

/* footer */
.footer-bg{left:0;top:3390px;z-index:3}
.foot{z-index:4;color:var(--white)}
.foot-brand{left:118px;top:3525px;display:flex;align-items:center;gap:10px;font-family:'Libre Baskerville',serif;font-weight:700;font-size:21px;line-height:1.25;width:220px}
.foot h4{font-size:15px;font-weight:600;letter-spacing:.2px}
.foot-list{font-size:15px;line-height:25.5px;font-weight:300}
.contact-item{display:flex;gap:14px;font-size:15px;line-height:27px;font-weight:300}
.copyright{left:0;width:1200px;top:3666px;text-align:center;font-size:13.5px;color:#b9b4a8;z-index:4;font-weight:300}
</style>
</head>
<body>

<!-- Hero -->
<div class="abs hero" role="img" aria-label="Mountain lake with a wooden jetty, reflected peaks and autumn larches"></div>
<div class="abs brand"><span class="brand-dot"></span>Quiet Harbor Path</div>
<nav class="abs nav">
  <a class="active" href="#">Home</a><a href="#">About</a><a href="#">Services</a><a href="#">Reviews</a><a href="#">Blog</a><a href="#">Contact</a>
</nav>
<a class="btn book" href="#">Book Now</a>
<h1 class="abs hero-title">QUIET HARBOR PATH</h1>
<p class="abs hero-sub">what might you find....Lessons Solutions Answers</p>
<svg class="abs chev" width="20" height="14" viewBox="0 0 20 14"><path d="M4 4l6 6 6-6" fill="none" stroke="#fff" stroke-width="2"/></svg>

<!-- About us -->
<svg class="abs about-bg" width="1200" height="620" viewBox="0 0 1200 620">
  <path d="M0 96 Q600 -30 1200 96 L1200 560 Q600 470 0 610 Z" fill="var(--cream)"/>
</svg>
<h2 class="abs serif-head about-head">ABOUT US</h2>
<p class="abs about-text">Sed ut perspiciatis unde omnis iste natus error sit voluptatem accusantium doloremque laudantium, totam rem aperiam, eaque ipsa quae ab illo inventore veritatis et quasi archi tecto beatae vitae dicta sunt explicabo. Nemo enim ipsam voluptatem quia voluptas.</p>
<div class="abs prints" role="img" aria-label="Faint trail of footprints decoration"></div>
<div class="abs about-photo" role="img" aria-label="Sunlit stone steps climbing through a mossy forest"></div>

<!-- About hypnotherapy -->
<h2 class="abs serif-head hyp-head">ABOUT HYPNOTHERAPY</h2>
<p class="abs hyp-script">Exploration of past lives and life between lives can reveal things related to one's current life</p>
<p class="abs hyp-text">Nam libero tempore, cum soluta nobis est eligendi optio cumque nihil impedit quo minus id quod maxime placeat facere possimus, omnis voluptas assumenda est, omnis dolor repellendus. Temporibus autem quibusdam et aut officiis debitis aut rerum necessitatibus saepe eve­niet ut et voluptates repudiandae sint et molestiae non recusandae. Itaque earum rerum hic tenetur a sapiente delectus.</p>
<a class="btn hyp-btn" href="#">Learn More</a>
<div class="abs hyp-back"></div>
<div class="abs hyp-photo" role="img" aria-label="Glowing bird rising from an open hand in warm light"></div>

<!-- Hypnosis can heal -->
<div class="abs heal"></div>
<h2 class="abs serif-head heal-head">HYPNOSIS CAN HEAL</h2>

<div class="cond" style="left:54px;top:1998px">
  <svg width="100" height="92" viewBox="0 0 100 92"><circle cx="58" cy="70" r="20" fill="var(--orange)"/><circle cx="43" cy="38" r="16" fill="none" stroke="#222" stroke-width="2.5"/><path d="M16 88v-12q0-14 27-14t27 14v12" fill="none" stroke="#222" stroke-width="2.5"/><circle cx="15" cy="18" r="10" fill="none" stroke="#222" stroke-width="2.2"/><circle cx="72" cy="18" r="10" fill="none" stroke="#222" stroke-width="2.2"/></svg>
  Anxiety
</div>
<div class="cond" style="left:267px;top:2050px">
  <svg width="100" height="92" viewBox="0 0 100 92"><circle cx="62" cy="64" r="22" fill="var(--orange)"/><path d="M30 6h20l-4 30 8 10-6 38H32l2-40-6-10z" fill="none" stroke="#222" stroke-width="2.5"/><path d="M64 26q8 10 0 20M72 20q12 16 0 32" fill="none" stroke="#222" stroke-width="2.2"/></svg>
  Pain Relief
</div>
<div class="cond" style="left:479px;top:1998px">
  <svg width="100" height="92" viewBox="0 0 100 92"><circle cx="66" cy="66" r="22" fill="var(--orange)"/><rect x="14" y="4" width="66" height="62" rx="8" fill="none" stroke="#222" stroke-width="2.5"/><rect x="30" y="12" width="34" height="14" fill="none" stroke="#222" stroke-width="2.2"/><path d="M66 54v20M58 66l8 8 8-8" fill="none" stroke="#222" stroke-width="2.5"/></svg>
  Weight Loss
</div>
<div class="cond" style="left:690px;top:2050px">
  <svg width="100" height="92" viewBox="0 0 100 92"><circle cx="66" cy="66" r="22" fill="var(--orange)"/><rect x="12" y="56" width="64" height="12" fill="none" stroke="#222" stroke-width="2.5"/><path d="M26 40l50 40M60 40q-8-12 4-20t4-16" fill="none" stroke="#222" stroke-width="2.5"/></svg>
  Smoking/Vaping<br>Cessation
</div>
<div class="cond" style="left:902px;top:1998px">
  <svg width="100" height="92" viewBox="0 0 100 92"><circle cx="66" cy="66" r="22" fill="var(--orange)"/><circle cx="30" cy="40" r="10" fill="none" stroke="#222" stroke-width="2.5"/><circle cx="62" cy="40" r="10" fill="none" stroke="#222" stroke-width="2.5"/><path d="M14 86V66q0-12 16-12t16 12v20M46 86V66q0-12 16-12t16 12v20M46 10l3 6 6 1-5 4 1 6-5-3-5 3 1-6-5-4 6-1z" fill="none" stroke="#222" stroke-width="2.2"/></svg>
  Self Confidence
</div>
<a class="btn heal-btn" href="#">Learn More</a>

<!-- Testimonials -->
<h2 class="abs serif-head say-head">WHAT OUR CLIENTS SAY</h2>

<div class="card" style="left:-158px">
  <div class="avatar" role="img" aria-label="Client portrait"></div>
  <div class="qmark" role="img" aria-label="Quotation mark decoration"></div>
  <div class="c-name">Laura Penwick</div>
  <div class="stars"><svg width="70" height="12" viewBox="0 0 70 12" fill="#f2c21b"><path d="M6 0l1.8 4 4.2.4-3.2 2.8 1 4.2L6 9.2 2.2 11.4l1-4.2L0 4.4 4.2 4z"/><path transform="translate(14)" d="M6 0l1.8 4 4.2.4-3.2 2.8 1 4.2L6 9.2 2.2 11.4l1-4.2L0 4.4 4.2 4z"/><path transform="translate(28)" d="M6 0l1.8 4 4.2.4-3.2 2.8 1 4.2L6 9.2 2.2 11.4l1-4.2L0 4.4 4.2 4z"/><path transform="translate(42)" d="M6 0l1.8 4 4.2.4-3.2 2.8 1 4.2L6 9.2 2.2 11.4l1-4.2L0 4.4 4.2 4z"/><path transform="translate(56)" d="M6 0l1.8 4 4.2.4-3.2 2.8 1 4.2L6 9.2 2.2 11.4l1-4.2L0 4.4 4.2 4z"/></svg></div>
  <p class="c-text">Nemo enim ipsam voluptatem quia voluptas sit aspernatur aut odit aut fugit, sed quia consequuntur magni dolores eos qui ratione voluptatem sequi nesciunt <b>»</b></p>
  <div class="corner"></div>
</div>

<div class="card focus" style="left:363px">
  <div class="avatar" role="img" aria-label="Client portrait"></div>
  <div class="qmark" role="img" aria-label="Quotation mark decoration"></div>
  <div class="c-name">Laura Penwick</div>
  <div class="stars"><svg width="70" height="12" viewBox="0 0 70 12" fill="#f2c21b"><path d="M6 0l1.8 4 4.2.4-3.2 2.8 1 4.2L6 9.2 2.2 11.4l1-4.2L0 4.4 4.2 4z"/><path transform="translate(14)" d="M6 0l1.8 4 4.2.4-3.2 2.8 1 4.2L6 9.2 2.2 11.4l1-4.2L0 4.4 4.2 4z"/><path transform="translate(28)" d="M6 0l1.8 4 4.2.4-3.2 2.8 1 4.2L6 9.2 2.2 11.4l1-4.2L0 4.4 4.2 4z"/><path transform="translate(42)" d="M6 0l1.8 4 4.2.4-3.2 2.8 1 4.2L6 9.2 2.2 11.4l1-4.2L0 4.4 4.2 4z"/><path transform="translate(56)" d="M6 0l1.8 4 4.2.4-3.2 2.8 1 4.2L6 9.2 2.2 11.4l1-4.2L0 4.4 4.2 4z"/></svg></div>
  <p class="c-text">Nemo enim ipsam voluptatem quia voluptas sit aspernatur aut odit aut fugit, sed quia consequuntur magni dolores eos qui ratione voluptatem sequi nesciunt <b>»</b></p>
  <div class="corner"></div>
</div>

<div class="card" style="left:889px">
  <div class="avatar" role="img" aria-label="Client portrait"></div>
  <div class="qmark" role="img" aria-label="Quotation mark decoration"></div>
  <div class="c-name">Laura Penwick</div>
  <div class="stars"><svg width="70" height="12" viewBox="0 0 70 12" fill="#f2c21b"><path d="M6 0l1.8 4 4.2.4-3.2 2.8 1 4.2L6 9.2 2.2 11.4l1-4.2L0 4.4 4.2 4z"/><path transform="translate(14)" d="M6 0l1.8 4 4.2.4-3.2 2.8 1 4.2L6 9.2 2.2 11.4l1-4.2L0 4.4 4.2 4z"/><path transform="translate(28)" d="M6 0l1.8 4 4.2.4-3.2 2.8 1 4.2L6 9.2 2.2 11.4l1-4.2L0 4.4 4.2 4z"/><path transform="translate(42)" d="M6 0l1.8 4 4.2.4-3.2 2.8 1 4.2L6 9.2 2.2 11.4l1-4.2L0 4.4 4.2 4z"/><path transform="translate(56)" d="M6 0l1.8 4 4.2.4-3.2 2.8 1 4.2L6 9.2 2.2 11.4l1-4.2L0 4.4 4.2 4z"/></svg></div>
  <p class="c-text">Nemo enim ipsam voluptatem quia voluptas sit aspernatur aut odit aut fugit, sed quia consequuntur magni dolores eos qui ratione voluptatem sequi nesciunt <b>»</b></p>
  <div class="corner"></div>
</div>

<!-- Get a quote -->
<div class="abs quote-photo" role="img" aria-label="Two hikers on a rocky ridge above an alpine lake and snowy mountains"></div>
<svg class="abs arrows" width="120" height="46" viewBox="0 0 120 46">
  <circle cx="22" cy="23" r="20" fill="#fff" stroke="#cfcfcf" stroke-width="2"/>
  <path d="M31 23H14M20 17l-6 6 6 6" fill="none" stroke="#cfcfcf" stroke-width="2"/>
  <circle cx="100" cy="23" r="20" fill="#fff" stroke="var(--orange)" stroke-width="2.5"/>
  <path d="M91 23h17M102 17l6 6-6 6" fill="none" stroke="var(--orange)" stroke-width="2.5"/>
</svg>
<h2 class="abs serif-head quote-head">GET A QUOTE</h2>
<div class="field" style="top:3126px;height:46px">Name</div>
<div class="field" style="top:3181px;height:46px">Email ID</div>
<div class="field" style="top:3237px;height:81px">Message</div>
<a class="btn quote-btn" href="#">Learn More</a>

<!-- Footer -->
<svg class="abs footer-bg" width="1200" height="320" viewBox="0 0 1200 320">
  <path d="M0 70 Q600 -30 1200 70 L1200 320 L0 320 Z" fill="var(--footer)"/>
</svg>
<div class="abs foot foot-brand"><span class="brand-dot"></span>Quiet Harbor Path</div>

<div class="abs foot" style="left:389px;top:3463px">
  <h4>CONTACT INFO</h4>
  <div class="contact-item" style="margin-top:22px">
    <svg width="18" height="18" viewBox="0 0 24 24" style="margin-top:4px"><path d="M6.6 10.8a15 15 0 006.6 6.6l2.2-2.2c.3-.3.7-.4 1-.2 1.1.4 2.3.6 3.6.6.6 0 1 .4 1 1V20c0 .6-.4 1-1 1A17 17 0 013 4c0-.6.4-1 1-1h3.5c.6 0 1 .4 1 1 0 1.3.2 2.5.6 3.6.1.3 0 .7-.2 1z" fill="var(--orange)"/></svg>
    <span>Phone:<br>+1 555-010-2040</span>
  </div>
  <div class="contact-item" style="margin-top:12px">
    <svg width="18" height="18" viewBox="0 0 24 24" style="margin-top:4px"><path d="M3 5h18v14H3z" fill="var(--orange)"/><path d="M3 5l9 7 9-7" fill="none" stroke="var(--footer)" stroke-width="1.6"/></svg>
    <span>Email Id:<br>hello@quietharborpath.com</span>
  </div>
</div>

<div class="abs foot" style="left:742px;top:3463px">
  <h4>QUICK LINKS</h4>
  <div class="foot-list" style="margin-top:14px">Home<br>Apout<br>Services<br>Reviews<br>Blog</div>
</div>
<div class="abs foot" style="left:933px;top:3463px">
  <h4>OTHER LINKS</h4>
  <div class="foot-list" style="margin-top:14px">Contact Us<br>Terms &amp; Conditions<br>Privacy Policy</div>
</div>
<p class="abs copyright">Copyright © 2023 Quiet Harbor Path. All Rights Reserved.</p>

</body>
</html>
```